Flaschenetikett Fenno`s ColaMix
Zielgruppe
Wir machen einen ColaMix, weil wir es können und ihm eine Prise 80er verpassen wollen.
Hip, Trendig und ein bisschen Oldschool.
Bei uns kommt nur in die Flasche, was uns selber schmeckt und dabei preislich fair ist! Kein Schnickschnack, dafür mit viel Geschmack und einer Portion Oldschool.
Einfach einen richtig guten Brausa ähhmm, ColaMix!
Farben:
orange / weiss (Hintergrund Orange & Schrift Weiss)
oder
weiss / anthrazit
Flaschenfarbe:
braun
Etikettgröße:
max. 10 x 10 cm
Name:
Fennos ColaMix
Zusatztext:
MÜNCHEN
ColaMix (muss irgendwo auf dem Etikett stehen)
Die Beispiele finden wir ultra hip, ein bisschen oldschool, trendig und genau richtig. Alles simpel, kein BlimBlim aber dafür einen ziemlich hohen Stylfaktor.
Wir sind nicht modern, sondern Kinder der 80iger, stehen auf Industrie Vintage Zeug und brauchen einen "ColaMix" der zu uns passt.
Fenno, ja einfach Fenno soll er heissen. Ein deutscher Trendname aus dem 19.Jahrhundert und doch jung und frisch! Genau wie unser ColaMix.
Das Kultgetränk das Allen schmeckt kommt in einer Oldschool braunen Flasche um die Ecke.
WIR MACHEN UNS FAST IN DIE HOSEN VOR AUFREGUNG, WAS IHR SO AUF DER FLASCHE HABT!!!!
HAUT REIN!!!

```html
<!DOCTYPE html>
<html lang="de">
<head>
<meta charset="utf-8">
<title>Fenno's ColaMix – Flaschenetiketten</title>
<link rel="stylesheet" href="https://fonts.googleapis.com/css2?family=Yellowtail&family=Lobster&family=Libre+Baskerville:wght@700&family=Signika:wght@600&family=Yanone+Kaffeesatz:wght@500&display=swap">
<style>
  :root {
    --orange: #ef843c;
    --orange-soft: #f7c9a6;
    --paper: #ffffff;
    --stage: #efefef;
  }
  * { margin: 0; padding: 0; box-sizing: border-box; }
  html, body { width: 1200px; height: 857px; overflow: hidden; background: var(--stage); }
  .stage {
    width: 1200px; height: 857px;
    display: flex; align-items: center; justify-content: center; gap: 40px;
  }
  .label {
    position: relative;
    width: 540px; height: 540px;
    background: var(--paper);
    color: var(--orange);
    box-shadow: 0 2px 10px rgba(0,0,0,.12);
    overflow: hidden;
  }
  .rays {
    position: absolute; left: 40px; right: 40px; height: 46px;
    background: linear-gradient(to bottom, var(--paper), var(--orange-soft));
    opacity: .7;
  }
  .rays--top { top: 14px; }
  .rays--bottom { top: 454px; transform: scaleY(-1); }
  .band {
    position: absolute; left: 0; right: 0; height: 12px;
    background: var(--orange);
  }
  .band--top { top: 64px; }
  .band--bottom { top: 438px; }
  .brand-name {
    position: absolute; left: 20px; right: 20px; top: 92px;
    text-align: center;
    font-family: "Yellowtail", cursive;
    font-weight: 400;
    font-size: 120px; line-height: 1.1;
    white-space: nowrap;
    transform: rotate(-3deg);
  }
  .product-line {
    position: absolute; left: 0; right: 0; top: 262px;
    display: flex; justify-content: center; align-items: baseline; gap: 10px;
    padding-left: 60px;
  }
  .product-name {
    font-family: "Lobster", cursive;
    font-size: 50px; line-height: 1;
    letter-spacing: 1px;
  }
  .product-tag {
    font-family: "Libre Baskerville", serif;
    font-size: 13px; letter-spacing: 1px;
  }
  .since-row {
    position: absolute; left: 0; right: 0; top: 350px;
    display: flex; justify-content: center; align-items: center; gap: 22px;
    font-family: "Signika", sans-serif; font-size: 24px; line-height: 1;
  }
  .brand-mark {
    display: flex; align-items: center; gap: 10px;
  }
  .brand-mark__dot {
    width: 40px; height: 40px; border-radius: 50%; background: var(--orange);
  }
  .brand-mark__name {
    font-family: "Signika", sans-serif; font-size: 24px;
  }
  .origin {
    position: absolute; left: 0; right: 0; top: 504px;
    text-align: center;
    font-family: "Yanone Kaffeesatz", sans-serif; font-style: italic;
    font-size: 26px; line-height: 1;
  }
  .label--place .band--bottom { top: 470px; }
  .label--place .rays--bottom { top: 486px; }
  .place-block {
    position: absolute; left: 0; right: 0; top: 340px;
    display: flex; flex-direction: column; align-items: center; gap: 22px;
    font-family: "Signika", sans-serif; line-height: 1;
  }
  .place-block__line { font-size: 20px; letter-spacing: 1px; }
</style>
</head>
<body>
<main class="stage">

  <section class="label label--since">
    <div class="rays rays--top" role="img" aria-label="Strahlenkranz über dem oberen Balken"></div>
    <div class="band band--top"></div>
    <h1 class="brand-name">Fenno's</h1>
    <p class="product-line">
      <span class="product-name">Cola Mix</span>
      <span class="product-tag">ORIGINAL</span>
    </p>
    <div class="since-row">
      <span>SINCE</span>
      <span class="brand-mark">
        <span class="brand-mark__dot"></span>
        <span class="brand-mark__name">Fenno's</span>
      </span>
      <span>2016</span>
    </div>
    <div class="band band--bottom"></div>
    <div class="rays rays--bottom" role="img" aria-label="Strahlenkranz unter dem unteren Balken"></div>
    <p class="origin">Made for MUNICH</p>
  </section>

  <section class="label label--place">
    <div class="rays rays--top" role="img" aria-label="Strahlenkranz über dem oberen Balken"></div>
    <div class="band band--top"></div>
    <h1 class="brand-name">Fenno's</h1>
    <p class="product-line">
      <span class="product-name">Cola Mix</span>
      <span class="product-tag">ORIGINAL</span>
    </p>
    <div class="place-block">
      <p class="place-block__line">MADE FOR MUNICH</p>
      <span class="brand-mark">
        <span class="brand-mark__dot"></span>
        <span class="brand-mark__name">Fenno's</span>
      </span>
    </div>
    <div class="band band--bottom"></div>
    <div class="rays rays--bottom" role="img" aria-label="Strahlenkranz unter dem unteren Balken"></div>
  </section>

</main>
</body>
</html>
```